goal design

We are rolling out a goal for the next 3 years. the goal is as follows:
2014: $8 million gross profit, $1.25 million net income
2015: $12 million gross profit, $2.4 million net income
2016 $15 million gross profit, $4 million net income
We want a design that captures these numbers and that we can publish company wide that will quickly remind everyone of these goals. Our website is www.brookvalerecruiting.example. This will be an internal campaign. We will use the simple design to remind our people of our goals for the next 3 years. We will print it on mouse pads, shirts and things of this nature periodically to keep it front of mind for our people. So easy to remember, visually appealing and simple are good guidelines.
Updates
Target Market(s)
This is an internal campaign. it is to remind our people of our goals for the next few years so will be on little reminder items (i.e. cell phone covers, mouse pads, shirts, screen savers, etc).
Industry/Entity Type
It Company
Look and feel

```html
<!DOCTYPE html>
<html lang="en">
<head>
<meta charset="utf-8">
<title>2014 Goal</title>
<link href="https://fonts.googleapis.com/css2?family=Exo+2:wght@800;900&family=Crimson+Text:wght@400&display=swap" rel="stylesheet">
<style>
  :root {
    --bg: #f3f3f3;
    --navy: #1b4a79;
    --navy-deep: #163f69;
    --band: #8ea4cb;
    --white: #ffffff;
    --target-red: #e0262b;
  }
  * { margin: 0; padding: 0; box-sizing: border-box; }
  html, body { width: 1200px; height: 1200px; overflow: hidden; background: var(--bg); }
  .goal-card { position: relative; width: 1200px; height: 1200px; background: radial-gradient(circle at 50% 45%, #fafafa 0%, var(--bg) 70%); }
  .ribbon { position: absolute; left: 0; top: 0; width: 1200px; height: 1200px; }
  .fold { fill: var(--navy); }
  .fold-dark { fill: var(--navy-deep); }
  .band { fill: var(--band); }
  .target { position: absolute; left: 0; top: 0; }
  .year {
    position: absolute; left: 188px; top: 69px;
    font-family: "Exo 2", sans-serif; font-weight: 900; font-size: 281px; line-height: 1;
    color: var(--navy); letter-spacing: -5px;
  }
  .figure, .label {
    position: absolute; line-height: 1; white-space: nowrap;
    transform: rotate(-4deg); transform-origin: left top;
  }
  .figure { font-family: "Crimson Text", serif; font-weight: 400; color: var(--navy); }
  .figure sup { font-size: 0.5em; vertical-align: 0.75em; margin-right: 2px; }
  .label { font-family: "Exo 2", sans-serif; font-weight: 900; color: var(--white); letter-spacing: 1px; }
  .gross-figure { left: 192px; top: 338px; font-size: 158px; letter-spacing: 5px; }
  .gross-label  { left: 196px; top: 458px; font-size: 96px; }
  .net-figure   { left: 284px; top: 640px; font-size: 158px; letter-spacing: 2px; }
  .net-label    { left: 290px; top: 770px; font-size: 110px; }
</style>
</head>
<body>
<main class="goal-card">
  <svg class="ribbon" viewBox="0 0 1200 1200" aria-hidden="true">
    <polygon class="fold-dark" points="842,196 915,196 1078,600 1072,660 264,690 168,560"/>
    <polygon class="fold" points="272,740 280,900 140,1095 178,995 90,1000"/>
    <polygon class="band" points="172,358 884,308 900,523 168,568"/>
    <polygon class="band" points="264,653 1070,597 1078,833 272,889"/>
  </svg>

  <svg class="target" width="200" height="400" viewBox="0 0 200 400" aria-hidden="true">
    <circle cx="131" cy="272" r="58" fill="var(--target-red)"/>
    <circle cx="131" cy="272" r="42" fill="var(--white)"/>
    <circle cx="131" cy="272" r="29" fill="var(--target-red)"/>
    <circle cx="131" cy="272" r="15" fill="var(--white)"/>
    <circle cx="131" cy="272" r="7" fill="var(--target-red)"/>
  </svg>

  <div class="year">2014</div>

  <div class="figure gross-figure"><sup>$</sup>8 million</div>
  <div class="label gross-label">GROSS PROFIT</div>

  <div class="figure net-figure"><sup>$</sup>1.25 million</div>
  <div class="label net-label">NET INCOME</div>
</main>
</body>
</html>
```